Customer Dashboard Design for Email Security SaaS

Mailbrook is a commercial email spam filter offered as a SaaS product, built and operated by a small German hosting provider. It protects business email accounts against spam, phishing, scam, and viruses using a multilayer filtering pipeline that combines traditional spam detection with AI-powered classification. The product runs entirely on German infrastructure, ensuring data sovereignty for European customers.

We need a complete redesign of the customer-facing dashboard. This is the web application where paying customers manage their email filtering: view their mail log, check quarantined emails, manage allow/blocklists, configure their settings, and handle their subscription. It is the primary touchpoint between Mailbrook and its customers.

Our customers are system administrators, IT managers at small-to-medium businesses, and operators of small hosting providers. They are technically competent but not designers. They expect professional, efficient tools that respect their time. They typically manage 10–500 email accounts and check the dashboard a few times per week, with heavier use during spam incidents.

We have attached the current mockups which really need to be replaced with something good looking.

Target Market(s)

System administrators, IT managers at small-to-medium businesses, and operators of small hosting providers.

Industry/Entity Type

SaaS

Number of Pages Required

5+ page

```html
<!DOCTYPE html>
<html lang="de">
<head>
<meta charset="utf-8">
<title>Mailbrook – Kunden-Dashboard</title>
<link href="https://fonts.googleapis.com/css2?family=Inter:wght@300;400;500;600;700&display=swap" rel="stylesheet">
<style>
:root{
  --canvas:#8f9190;
  --bg:#0f1111;
  --side:#0a0b0b;
  --card:#151717;
  --card-2:#1b1d1d;
  --line:#252828;
  --text:#f2f4f3;
  --muted:#9aa19e;
  --dim:#6b7370;
  --green:#149a68;
  --green-2:#1fb47b;
  --green-dark:#0e4d37;
  --red:#b8232a;
  --red-text:#e0363d;
  --orange:#e39a1c;
  --blue:#2aa3d8;
  --ham:#27c26c;
}
*{box-sizing:border-box;margin:0;padding:0}
html,body{width:1200px;height:640px;overflow:hidden;background:var(--canvas)}
body{position:relative;font-family:"Inter",sans-serif;color:var(--text)}
.screen{position:absolute;width:797px;background:var(--bg);transform-origin:0 0;transform:scale(.4658);overflow:hidden}
.screen *{position:absolute}
.screen table *{position:static}
.screen table.log-table{position:absolute}
.topbar{left:0;top:0;width:797px;height:42px;border-bottom:1px solid var(--line);background:var(--bg)}
.brand{left:12px;top:11px;width:110px;height:20px}
.brand-dot{left:0;top:1px;width:18px;height:18px;border-radius:50%;background:var(--green)}
.brand-name{left:26px;top:3px;font-size:9px;font-weight:700;white-space:nowrap}
.greeting{left:148px;top:10px;font-size:8px;font-weight:700;white-space:nowrap}
.mode{left:148px;top:24px;font-size:5px;color:var(--muted);white-space:nowrap}
.chat{left:628px;top:11px;width:20px;height:20px;border-radius:50%;background:#fff}
.chat i{top:9px;width:3px;height:3px;border-radius:50%;background:#111}
.bell{left:660px;top:12px;width:18px;height:18px}
.bell-badge{left:671px;top:10px;width:11px;height:11px;border-radius:50%;background:var(--green);border:1px solid #dfe;font-size:5px;line-height:9px;text-align:center;font-style:normal}
.avatar{left:697px;top:8px;width:26px;height:26px;border-radius:50%;background:radial-gradient(circle at 50% 40%,#e7c3a4,#a8694a 70%);border:1px solid #333}
.user{left:729px;top:16px;font-size:6.5px;white-space:nowrap}
.caret{left:780px;top:17px;width:7px;height:7px}
.sidebar{left:0;top:42px;width:130px;bottom:0;background:var(--side);border-right:1px solid var(--line)}
.nav{left:0;top:9px;width:130px;list-style:none}
.nav li{position:relative;height:22px;font-size:6.5px;line-height:22px;padding-left:26px;white-space:nowrap;color:var(--text)}
.nav li svg{left:11px;top:7px;width:8px;height:8px}
.nav li.active{color:var(--green-2);background:linear-gradient(90deg,#0d241b,transparent)}
.nav li.active::before{content:"";position:absolute;left:0;top:4px;width:2px;height:14px;background:var(--green-2)}
.page-title{left:148px;top:53px;font-size:12px;font-weight:300;white-space:nowrap}
.page-desc{left:148px;top:75px;font-size:7.5px;line-height:13px;color:var(--muted);width:320px}
.card{background:var(--card);border:1px solid var(--line);border-radius:6px}
.btn{font-size:6.5px;line-height:19px;text-align:center;border-radius:3px;color:#fff;white-space:nowrap}
.btn-green{background:var(--green)}
.btn-red{background:var(--red)}
.btn-ghost{background:#1d2020;border:1px solid var(--line)}
.input{background:#1e2121;border:1px solid #272a2a;border-radius:3px;font-size:6.5px;color:var(--dim);padding-left:10px;white-space:nowrap}
.stat{height:99px;width:205px;top:53px;overflow:hidden}
.stat::after{content:"";position:absolute;left:10px;right:10px;bottom:0;height:2px;background:linear-gradient(90deg,transparent,var(--green),transparent)}
.stat-icon{left:12px;top:12px;width:14px;height:14px;border:1px solid var(--green);border-radius:3px;background:#0e2a1f}
.stat-label{left:36px;top:15px;font-size:7.5px;letter-spacing:.3px;white-space:nowrap}
.stat-value{left:12px;top:40px;font-size:23px;font-weight:700}
.stat-note{left:12px;top:78px;font-size:7px;white-space:nowrap}
.axis-y{left:160px;font-size:10px;color:#ddd}
.axis-x{top:449px;font-size:8.5px;color:var(--muted);white-space:nowrap}
.action{top:487px;width:311px;height:133px;overflow:hidden}
.action-icon{left:12px;top:14px;width:14px;height:14px;border:1px solid var(--green);border-radius:3px;background:#0e2a1f}
.action-title{left:12px;top:43px;font-size:13px;font-weight:700;white-space:nowrap}
.action-text{left:12px;top:63px;width:160px;font-size:6.5px;line-height:10px}
.action .btn{left:12px;top:96px;width:108px;height:25px;line-height:25px;font-size:7.5px}
.action-art{top:20px;width:100px;height:95px;border-radius:50%;background:radial-gradient(circle,#2a2e2d,transparent 70%);opacity:.8}
.label-cap{font-size:4.5px;color:var(--dim);letter-spacing:.5px;white-space:nowrap}
.log-table{left:160px;top:199px;width:608px;border-collapse:collapse;font-size:6.5px;table-layout:fixed}
.log-table th{height:32px;text-align:left;padding-left:10px;font-size:8px;font-weight:600;background:#1a1c1c;border-right:1px solid var(--line)}
.log-table td{height:33px;padding-left:10px;border-top:1px solid var(--line);border-right:1px solid var(--line);white-space:nowrap;overflow:hidden}
.log-table td:last-child,.log-table th:last-child{border-right:none}
.v-ham{color:var(--ham)}.v-spam{color:var(--red-text)}.v-phish{color:var(--orange)}.v-virus{color:var(--blue)}
.chev{float:right;margin-right:8px}
.pager{font-size:7px;color:var(--muted);top:468px;white-space:nowrap}
.q-card{width:310px;height:141px}
.q-from{left:11px;top:16px;font-size:8px;white-space:nowrap}
.pill{top:12px;right:11px;height:17px;width:62px;border-radius:3px;background:#1f1a12;font-size:6px;line-height:17px;text-align:center;white-space:nowrap}
.q-subject{left:11px;top:52px;font-size:8.5px;font-weight:600;white-space:nowrap}
.q-date{left:11px;top:79px;font-size:6px;white-space:nowrap}
.q-score{right:11px;top:79px;font-size:6px}
.q-check{left:11px;top:115px;width:8px;height:8px;border:1px solid #555;border-radius:2px}
.row-mail{left:160px;font-size:8px;white-space:nowrap}
.row-sep{left:160px;width:608px;height:1px;background:var(--line)}
.row-btn{left:713px;width:55px;height:19px}
.opt{top:513px;width:194px;height:69px;background:var(--card-2);border:1px solid var(--line);border-radius:4px}
.opt-title{left:11px;top:33px;font-size:7px;white-space:nowrap}
.opt-desc{left:11px;top:48px;font-size:4.5px;color:var(--muted);white-space:nowrap}
.opt-radio{right:10px;top:10px;width:8px;height:8px;border-radius:50%;border:1px solid #555}
.opt svg{left:11px;top:10px;width:11px;height:11px}
.card-title{font-size:11px;font-weight:400;white-space:nowrap}
.card-text{font-size:7px;color:var(--muted);white-space:nowrap;letter-spacing:.2px}
</style>
</head>
<body>

<section class="screen" style="left:15.8px;top:38.7px;height:714px">
  <header class="topbar">
    <div class="brand"><span class="brand-dot"></span><span class="brand-name">Mailbrook</span></div>
    <p class="greeting">Guten Tag, Lena Hartmann</p>
    <p class="mode">Beobachtungsmodus - Mails werden analysiert aber nicht blockiert</p>
    <span class="chat"><i style="left:5px"></i><i style="left:9px"></i><i style="left:13px"></i></span>
    <svg class="bell" viewBox="0 0 18 18"><path d="M9 2a5 5 0 0 1 5 5v4l2 3H2l2-3V7a5 5 0 0 1 5-5zM7 15a2 2 0 0 0 4 0z" fill="#fff"/></svg>
    <i class="bell-badge">9</i>
    <span class="avatar" role="img" aria-label="Profilfoto des Nutzers"></span>
    <span class="user">Lena Hartmann</span>
    <svg class="caret" viewBox="0 0 8 8"><path d="M1 2.5 4 5.5 7 2.5" stroke="#fff" fill="none"/></svg>
  </header>
  <aside class="sidebar">
    <ul class="nav">
      <li class="active"><svg viewBox="0 0 8 8"><path d="M0 0h3v3H0zM5 0h3v3H5zM0 5h3v3H0zM5 5h3v3H5z" fill="currentColor"/></svg>Dashboard</li>
      <li><svg viewBox="0 0 8 8"><path d="M0 1h8M0 4h8M0 7h8" stroke="currentColor"/></svg>Mail-Log</li>
      <li><svg viewBox="0 0 8 8"><path d="M4 .5 7 2v2.5C7 6 5.5 7.2 4 7.6 2.5 7.2 1 6 1 4.5V2z" stroke="currentColor" fill="none"/></svg>Quarantine</li>
      <li><svg viewBox="0 0 8 8"><rect x=".5" y="1.5" width="7" height="5.5" rx="1" stroke="currentColor" fill="none"/></svg>Mailbox Quota</li>
      <li><svg viewBox="0 0 8 8"><circle cx="4" cy="4" r="3" stroke="currentColor" fill="none"/><circle cx="4" cy="4" r="1" fill="currentColor"/></svg>Settings</li>
      <li><svg viewBox="0 0 8 8"><rect x="1" y="3.5" width="6" height="4" stroke="currentColor" fill="none"/><path d="M2.5 3.5V2a1.5 1.5 0 0 1 3 0v1.5" stroke="currentColor" fill="none"/></svg>Paywall Overlay</li>
      <li><svg viewBox="0 0 8 8"><rect x=".5" y=".5" width="7" height="7" stroke="currentColor" fill="none"/><path d="M3 .5v7" stroke="currentColor"/></svg>Navigation Shell</li>
    </ul>
  </aside>

  <div class="card stat" style="left:148px"><span class="stat-icon"></span><span class="stat-label">SPAM &amp; BEDROHUNGEN</span><span class="stat-value">4,202</span><span class="stat-note">Spam, Phishing und Viren erfolgreich blockiert</span></div>
  <div class="card stat" style="left:362px"><span class="stat-icon"></span><span class="stat-label">NEWSLETTER &amp; SONSTIGES</span><span class="stat-value">2,100</span><span class="stat-note">Automatisch kategorisierte E-Mails</span></div>
  <div class="card stat" style="left:575px"><span class="stat-icon"></span><span class="stat-label">IN QUARANTÄNE</span><span class="stat-value">56</span><span class="stat-note">Zur Überprüfung bereit</span></div>

  <div class="card" style="left:148px;top:164px;width:632px;height:310px"></div>
  <p style="left:160px;top:175px;font-size:8px;font-weight:700">E-Mail Aktivität</p>
  <p style="left:160px;top:189px;font-size:4.5px;color:var(--muted)">Letzte 7 / 30 Tage</p>
  <div class="btn btn-ghost" style="left:684px;top:177px;width:84px;height:26px;line-height:24px;font-size:6px;text-align:left;padding-left:12px">Letzte 30 Tage ⌄</div>
  <span class="axis-y" style="top:210px">1000</span><span class="axis-y" style="top:246px">800</span><span class="axis-y" style="top:281px">600</span><span class="axis-y" style="top:317px">450</span><span class="axis-y" style="top:352px">300</span><span class="axis-y" style="top:388px">150</span><span class="axis-y" style="top:424px">0</span>
  <svg style="left:195px;top:210px;width:575px;height:225px" viewBox="0 0 575 225">
    <defs><linearGradient id="area" x1="0" y1="0" x2="0" y2="1"><stop offset="0" stop-color="#149a68" stop-opacity=".75"/><stop offset="1" stop-color="#149a68" stop-opacity=".02"/></linearGradient></defs>
    <g stroke="#2a2e2d" stroke-dasharray="3 3"><path d="M0 7H575M0 43H575M0 78H575M0 114H575M0 149H575M0 185H575M0 221H575"/></g>
    <path d="M0,117 C12,105 22,100 33,110 C48,125 60,170 76,168 C92,166 105,150 121,142 C140,130 150,68 171,70 C185,72 195,108 211,110 C225,112 238,96 251,100 C270,106 288,148 306,142 C330,130 360,40 393,39 C420,38 438,98 451,97 C458,96 460,88 465,90 C474,94 478,117 486,115 C495,113 500,92 511,87 C522,82 533,80 541,62 C552,40 556,14 571,17 L571,221 L0,221 Z" fill="url(#area)"/>
    <path d="M0,117 C12,105 22,100 33,110 C48,125 60,170 76,168 C92,166 105,150 121,142 C140,130 150,68 171,70 C185,72 195,108 211,110 C225,112 238,96 251,100 C270,106 288,148 306,142 C330,130 360,40 393,39 C420,38 438,98 451,97 C458,96 460,88 465,90 C474,94 478,117 486,115 C495,113 500,92 511,87 C522,82 533,80 541,62 C552,40 556,14 571,17" fill="none" stroke="#1fb47b" stroke-width="2.5"/>
  </svg>
  <span class="axis-x" style="left:187px">Jan 23</span><span class="axis-x" style="left:235px">Feb 23</span><span class="axis-x" style="left:285px">Mar 14</span><span class="axis-x" style="left:333px">Apr 23</span><span class="axis-x" style="left:382px">May 23</span><span class="axis-x" style="left:436px">Jun 23</span><span class="axis-x" style="left:484px">Jul 23</span><span class="axis-x" style="left:530px">Aug 23</span><span class="axis-x" style="left:580px">Sept 23</span><span class="axis-x" style="left:634px">Oct 23</span><span class="axis-x" style="left:684px">Nov 23</span><span class="axis-x" style="left:734px">Dec 23</span>

  <div class="card action" style="left:148px">
    <span class="action-icon"></span>
    <p class="action-title">Quarantäne prüfen</p>
    <p class="action-text">Überprüfen Sie zurückgehaltene E-Mails und geben Sie diese bei Bedarf frei.</p>
    <span class="action-art" role="img" aria-label="Dekoratives Schild-Symbol" style="left:190px"></span>
    <span class="btn btn-green">Zur Quarantäne</span>
  </div>
  <div class="card action" style="left:468px">
    <span class="action-icon"></span>
    <p class="action-title">Mail-Log anzeigen</p>
    <p class="action-text">Sehen Sie alle verarbeiteten E-Mails und deren Status im Detail ein.</p>
    <span class="action-art" role="img" aria-label="Dekorative Dokument-Grafik" style="left:195px"></span>
    <span class="btn btn-green">Mail-Log Öffnen</span>
  </div>

  <div class="card" style="left:148px;top:632px;width:632px;height:65px"></div>
  <p style="left:160px;top:650px;font-size:12px;font-weight:700">Systemstatus</p>
  <p style="left:160px;top:673px;font-size:6.5px;white-space:nowrap">Alle Filter arbeiten einwandfrei. Letztes Update: 12.05.2024,14:32 Uhr</p>
  <span style="left:703px;top:670px;width:65px;height:11px;border-radius:6px;background:#143a2a;color:var(--green-2);font-size:4.5px;line-height:11px;text-align:center;white-space:nowrap">Alle Systeme aktiv</span>
</section>

<section class="screen" style="left:400.6px;top:38.7px;height:513px">
  <header class="topbar">
    <div class="brand"><span class="brand-dot"></span><span class="brand-name">Mailbrook</span></div>
    <p class="greeting">Guten Tag, Lena Hartmann</p>
    <p class="mode">Beobachtungsmodus - Mails werden analysiert aber nicht blockiert</p>
    <span class="chat"><i style="left:5px"></i><i style="left:9px"></i><i style="left:13px"></i></span>
    <svg class="bell" viewBox="0 0 18 18"><path d="M9 2a5 5 0 0 1 5 5v4l2 3H2l2-3V7a5 5 0 0 1 5-5zM7 15a2 2 0 0 0 4 0z" fill="#fff"/></svg>
    <i class="bell-badge">9</i>
    <span class="avatar" role="img" aria-label="Profilfoto des Nutzers"></span>
    <span class="user">Lena Hartmann</span>
    <svg class="caret" viewBox="0 0 8 8"><path d="M1 2.5 4 5.5 7 2.5" stroke="#fff" fill="none"/></svg>
  </header>
  <aside class="sidebar">
    <ul class="nav">
      <li><svg viewBox="0 0 8 8"><path d="M0 0h3v3H0zM5 0h3v3H5zM0 5h3v3H0zM5 5h3v3H5z" fill="currentColor"/></svg>Dashboard</li>
      <li class="active"><svg viewBox="0 0 8 8"><path d="M0 1h8M0 4h8M0 7h8" stroke="currentColor"/></svg>Mail-Log</li>
      <li><svg viewBox="0 0 8 8"><path d="M4 .5 7 2v2.5C7 6 5.5 7.2 4 7.6 2.5 7.2 1 6 1 4.5V2z" stroke="currentColor" fill="none"/></svg>Quarantine</li>
      <li><svg viewBox="0 0 8 8"><rect x=".5" y="1.5" width="7" height="5.5" rx="1" stroke="currentColor" fill="none"/></svg>Mailbox Quota</li>
      <li><svg viewBox="0 0 8 8"><circle cx="4" cy="4" r="3" stroke="currentColor" fill="none"/><circle cx="4" cy="4" r="1" fill="currentColor"/></svg>Settings</li>
      <li><svg viewBox="0 0 8 8"><rect x="1" y="3.5" width="6" height="4" stroke="currentColor" fill="none"/><path d="M2.5 3.5V2a1.5 1.5 0 0 1 3 0v1.5" stroke="currentColor" fill="none"/></svg>Paywall Overlay</li>
      <li><svg viewBox="0 0 8 8"><rect x=".5" y=".5" width="7" height="7" stroke="currentColor" fill="none"/><path d="M3 .5v7" stroke="currentColor"/></svg>Navigation Shell</li>
    </ul>
  </aside>
  <h1 class="page-title">Mail-Log</h1>
  <p class="page-desc">Deep inspection of enterprise inbound and outbound traffic. Analysis based on Sentinel curator scoring.</p>
  <span class="btn btn-green" style="left:627px;top:81px;width:71px;height:19px">⤓ Export Logs</span>
  <span class="btn btn-ghost" style="left:706px;top:81px;width:73px;height:19px">↻ Refresh Data</span>

  <div class="card" style="left:148px;top:120px;width:632px;height:50px;background:#131515"></div>
  <span class="label-cap" style="left:160px;top:132px">DATE RANGE</span>
  <span class="label-cap" style="left:292px;top:132px">VERDICT</span>
  <span class="label-cap" style="left:378px;top:132px">SENDER / DOMAIN</span>
  <span class="input" style="left:160px;top:145px;width:124px;height:19px;line-height:17px;color:var(--text);font-size:6px;padding-left:6px">▣ Oct 24, 2023 - Oct 31, 2023</span>
  <span class="input" style="left:292px;top:145px;width:77px;height:19px;line-height:17px;color:var(--text);font-size:6px;padding-left:6px">All Verdicts ⌄</span>
  <span class="input" style="left:378px;top:145px;width:311px;height:19px;line-height:17px;font-size:6px">Filter by address...</span>
  <span class="btn btn-green" style="left:697px;top:145px;width:71px;height:19px">Apply Filters</span>

  <div class="card" style="left:148px;top:188px;width:632px;height:253px"></div>
  <table class="log-table">
    <colgroup><col style="width:67px"><col style="width:103px"><col style="width:102px"><col style="width:102px"><col style="width:102px"><col style="width:66px"><col style="width:66px"></colgroup>
    <thead><tr><th>S.No</th><th>Zeit</th><th>Absender</th><th>Empfänger</th><th>Betreff</th><th>Verdict</th><th>Score</th></tr></thead>
    <tbody>
      <tr><td>01</td><td>13.04.2026, 15:13</td><td>info@nordwerk.de</td><td>info@nordwerk.de</td><td>Invoice for March</td><td class="v-ham">Ham<span class="chev">⌄</span></td><td>0.0 – 10.0</td></tr>
      <tr><td>02</td><td>14.04.2026, 09:45</td><td>info@nordwerk.de</td><td>info@nordwerk.de</td><td>Invoice for March</td><td class="v-spam">Spam<span class="chev">⌄</span></td><td>0.0 – 10.0</td></tr>
      <tr><td>03</td><td>15.04.2026, 11:30</td><td>info@nordwerk.de</td><td>info@nordwerk.de</td><td>Invoice for March</td><td class="v-phish">Phishing<span class="chev">⌄</span></td><td>8.5 – 10.0</td></tr>
      <tr><td>04</td><td>16.04.2026, 14:22</td><td>info@nordwerk.de</td><td>info@nordwerk.de</td><td>Invoice for March</td><td class="v-virus">Virus<span class="chev">⌄</span></td><td>7.0 – 10.0</td></tr>
      <tr><td>05</td><td>17.04.2026, 08:55</td><td>info@nordwerk.de</td><td>info@nordwerk.de</td><td>Invoice for March</td><td class="v-ham">Ham<span class="chev">⌄</span></td><td>9.0 – 10.0</td></tr>
      <tr><td>06</td><td>18.04.2026, 16:10</td><td>info@nordwerk.de</td><td>info@nordwerk.de</td><td>Invoice for March</td><td class="v-spam">Spam<span class="chev">⌄</span></td><td>7.5 – 10.0</td></tr>
    </tbody>
  </table>

  <div style="left:148px;top:455px;width:632px;height:35px;background:#131515;border-radius:4px"></div>
  <span class="pager" style="left:161px;font-size:4.5px;top:470px">Showing 1-25 of 12,482 entries</span>
  <span class="pager" style="left:615px">Previous</span>
  <span class="btn btn-green" style="left:662px;top:463px;width:17px;height:19px;line-height:19px">1</span>
  <span class="pager" style="left:691px">2</span>
  <span class="pager" style="left:716px">3</span>
  <span class="pager" style="left:740px">Next</span>
</section>

<section class="screen" style="left:781.1px;top:38.7px;height:513px">
  <header class="topbar">
    <div class="brand"><span class="brand-dot"></span><span class="brand-name">Mailbrook</span></div>
    <p class="greeting">Guten Tag, Lena Hartmann</p>
    <p class="mode">Beobachtungsmodus - Mails werden analysiert aber nicht blockiert</p>
    <span class="chat"><i style="left:5px"></i><i style="left:9px"></i><i style="left:13px"></i></span>
    <svg class="bell" viewBox="0 0 18 18"><path d="M9 2a5 5 0 0 1 5 5v4l2 3H2l2-3V7a5 5 0 0 1 5-5zM7 15a2 2 0 0 0 4 0z" fill="#fff"/></svg>
    <i class="bell-badge">9</i>
    <span class="avatar" role="img" aria-label="Profilfoto des Nutzers"></span>
    <span class="user">Lena Hartmann</span>
    <svg class="caret" viewBox="0 0 8 8"><path d="M1 2.5 4 5.5 7 2.5" stroke="#fff" fill="none"/></svg>
  </header>
  <aside class="sidebar">
    <ul class="nav">
      <li><svg viewBox="0 0 8 8"><path d="M0 0h3v3H0zM5 0h3v3H5zM0 5h3v3H0zM5 5h3v3H5z" fill="currentColor"/></svg>Dashboard</li>
      <li><svg viewBox="0 0 8 8"><path d="M0 1h8M0 4h8M0 7h8" stroke="currentColor"/></svg>Mail-Log</li>
      <li class="active"><svg viewBox="0 0 8 8"><path d="M4 .5 7 2v2.5C7 6 5.5 7.2 4 7.6 2.5 7.2 1 6 1 4.5V2z" stroke="currentColor" fill="none"/></svg>Quarantine</li>
      <li><svg viewBox="0 0 8 8"><rect x=".5" y="1.5" width="7" height="5.5" rx="1" stroke="currentColor" fill="none"/></svg>Mailbox Quota</li>
      <li><svg viewBox="0 0 8 8"><circle cx="4" cy="4" r="3" stroke="currentColor" fill="none"/><circle cx="4" cy="4" r="1" fill="currentColor"/></svg>Settings</li>
      <li><svg viewBox="0 0 8 8"><rect x="1" y="3.5" width="6" height="4" stroke="currentColor" fill="none"/><path d="M2.5 3.5V2a1.5 1.5 0 0 1 3 0v1.5" stroke="currentColor" fill="none"/></svg>Paywall Overlay</li>
      <li><svg viewBox="0 0 8 8"><rect x=".5" y=".5" width="7" height="7" stroke="currentColor" fill="none"/><path d="M3 .5v7" stroke="currentColor"/></svg>Navigation Shell</li>
    </ul>
  </aside>
  <h1 class="page-title">Quarantine</h1>
  <p class="page-desc">Manage intercepted communications. Your curated vault for suspicious activity requiring manual validation or systematic purge.</p>
  <span class="btn btn-green" style="left:710px;top:81px;width:69px;height:19px">☰ Filter Vault</span>

  <div style="left:148px;top:124px;width:632px;height:22px;border-bottom:1px solid var(--line)"></div>
  <span class="label-cap" style="left:160px;top:132px">☐ SELECT ALL &nbsp;&nbsp;|&nbsp;&nbsp; ⊘ RELEASE &nbsp;&nbsp; ▢ BULK PURGE &nbsp;&nbsp; ⊙ MARK SAFE</span>
  <span class="label-cap" style="left:654px;top:132px">SHOWING 4 ITEMS IN CURATION</span>

  <div class="card q-card" style="left:148px;top:162px">
    <span class="q-from">info@nordwerk.de</span><span class="pill v-phish">Phishing ⌄</span>
    <span class="q-subject">Urgent: Reset Your Password Now!</span>
    <span class="q-date">18.04.2026, 10:31</span><span class="q-score">9.2</span>
    <span class="q-check"></span>
    <span class="btn btn-green" style="left:179px;top:109px;width:55px;height:19px">Freigeben</span>
    <span class="btn btn-red" style="left:250px;top:109px;width:49px;height:19px">Löschen</span>
  </div>
  <div class="card q-card" style="left:469px;top:162px">
    <span class="q-from">info@nordwerk.de</span><span class="pill v-ham" style="background:#10231a">Ham ⌄</span>
    <span class="q-subject">Invoice for March 2026</span>
    <span class="q-date">18.04.2026, 10:31</span><span class="q-score">9.2</span>
    <span class="q-check"></span>
    <span class="btn btn-green" style="left:179px;top:109px;width:55px;height:19px">Freigeben</span>
    <span class="btn btn-red" style="left:250px;top:109px;width:49px;height:19px">Löschen</span>
  </div>
  <div class="card q-card" style="left:148px;top:314px">
    <span class="q-from">info@nordwerk.de</span><span class="pill v-spam" style="background:#231314">Spam ⌄</span>
    <span class="q-subject">Payment Failed – Action Required</span>
    <span class="q-date">18.04.2026, 10:31</span><span class="q-score">9.2</span>
    <span class="q-check"></span>
    <span class="btn btn-green" style="left:179px;top:109px;width:55px;height:19px">Freigeben</span>
    <span class="btn btn-red" style="left:250px;top:109px;width:49px;height:19px">Löschen</span>
  </div>
  <div class="card q-card" style="left:469px;top:314px">
    <span class="q-from">info@nordwerk.de</span><span class="pill v-virus" style="background:#111d24">Virus ⌄</span>
    <span class="q-subject">New Message from Support Team</span>
    <span class="q-date">18.04.2026, 10:31</span><span class="q-score">9.2</span>
    <span class="q-check"></span>
    <span class="btn btn-green" style="left:179px;top:109px;width:55px;height:19px">Freigeben</span>
    <span class="btn btn-red" style="left:250px;top:109px;width:49px;height:19px">Löschen</span>
  </div>
</section>

<section class="screen" style="left:400.6px;top:303.7px;height:590px">
  <header class="topbar">
    <div class="brand"><span class="brand-dot"></span><span class="brand-name">Mailbrook</span></div>
    <p class="greeting">Guten Tag, Lena Hartmann</p>
    <p class="mode">Beobachtungsmodus - Mails werden analysiert aber nicht blockiert</p>
    <span class="chat"><i style="left:5px"></i><i style="left:9px"></i><i style="left:13px"></i></span>
    <svg class="bell" viewBox="0 0 18 18"><path d="M9 2a5 5 0 0 1 5 5v4l2 3H2l2-3V7a5 5 0 0 1 5-5zM7 15a2 2 0 0 0 4 0z" fill="#fff"/></svg>
    <i class="bell-badge">9</i>
    <span class="avatar" role="img" aria-label="Profilfoto des Nutzers"></span>
    <span class="user">Lena Hartmann</span>
    <svg class="caret" viewBox="0 0 8 8"><path d="M1 2.5 4 5.5 7 2.5" stroke="#fff" fill="none"/></svg>
  </header>
  <aside class="sidebar">
    <ul class="nav">
      <li><svg viewBox="0 0 8 8"><path d="M0 0h3v3H0zM5 0h3v3H5zM0 5h3v3H0zM5 5h3v3H5z" fill="currentColor"/></svg>Dashboard</li>
      <li><svg viewBox="0 0 8 8"><path d="M0 1h8M0 4h8M0 7h8" stroke="currentColor"/></svg>Mail-Log</li>
      <li><svg viewBox="0 0 8 8"><path d="M4 .5 7 2v2.5C7 6 5.5 7.2 4 7.6 2.5 7.2 1 6 1 4.5V2z" stroke="currentColor" fill="none"/></svg>Quarantine</li>
      <li class="active"><svg viewBox="0 0 8 8"><rect x=".5" y="1.5" width="7" height="5.5" rx="1" stroke="currentColor" fill="none"/></svg>Mailbox Quota</li>
      <li><svg viewBox="0 0 8 8"><circle cx="4" cy="4" r="3" stroke="currentColor" fill="none"/><circle cx="4" cy="4" r="1" fill="currentColor"/></svg>Settings</li>
      <li><svg viewBox="0 0 8 8"><rect x="1" y="3.5" width="6" height="4" stroke="currentColor" fill="none"/><path d="M2.5 3.5V2a1.5 1.5 0 0 1 3 0v1.5" stroke="currentColor" fill="none"/></svg>Paywall Overlay</li>
      <li><svg viewBox="0 0 8 8"><rect x=".5" y=".5" width="7" height="7" stroke="currentColor" fill="none"/><path d="M3 .5v7" stroke="currentColor"/></svg>Navigation Shell</li>
    </ul>
  </aside>
  <h1 class="page-title">Postfächer</h1>
  <p class="page-desc" style="width:420px">Verwalten Sie Ihre geschützten E-Mail-Adressen und behalten Sie Ihr Kontingent im Blick.</p>
  <span class="label-cap" style="left:722px;top:59px">GLOBAL USAGE</span>
  <p style="left:708px;top:71px;font-size:12px;font-weight:600;white-space:nowrap">1.2 TB <span style="position:static;font-size:6px;font-weight:400;color:var(--muted)">/ 5.0 TB</span></p>

  <div class="card" style="left:148px;top:108px;width:632px;height:99px"></div>
  <p class="card-title" style="left:160px;top:120px">Kontingentübersicht</p>
  <p style="left:160px;top:152px;font-size:14px;white-space:nowrap">12 <span style="position:static;font-size:5px">von</span> 25 <span style="position:static;font-size:6px;color:var(--muted)">Postfächern verwendet</span></p>
  <span style="left:320px;top:157px;width:447px;height:8px;border-radius:4px;background:#232626"></span>
  <span style="left:320px;top:157px;width:214px;height:8px;border-radius:4px;background:var(--green)"></span>
  <p class="card-text" style="left:160px;top:187px">Sie nutzen aktuell 48% Ihres Kontingents.</p>

  <div class="card" style="left:148px;top:220px;width:632px;height:265px"></div>
  <p style="left:160px;top:233px;font-size:9px;font-weight:600">Geschützte Postfächer</p>
  <span class="row-sep" style="top:263px"></span>
  <span class="row-mail" style="top:280px">lena.hartmann@nordwerk.de</span><span class="btn btn-red row-btn" style="top:275px">Entfernen</span>
  <span class="row-sep" style="top:305px"></span>
  <span class="row-mail" style="top:322px">E-Mail-Adresse eingeben</span><span class="btn btn-red row-btn" style="top:317px">Entfernen</span>
  <span class="row-sep" style="top:347px"></span>
  <span class="row-mail" style="top:364px">lena.hartmann@nordwerk.de</span><span class="btn btn-red row-btn" style="top:359px">Entfernen</span>
  <span class="row-sep" style="top:389px"></span>
  <span class="row-mail" style="top:406px">E-Mail-Adresse eingeben</span><span class="btn btn-red row-btn" style="top:401px">Entfernen</span>
  <span class="row-sep" style="top:431px"></span>
  <span class="row-mail" style="top:448px">E-Mail-Adresse eingeben</span><span class="btn btn-red row-btn" style="top:443px">Entfernen</span>
  <span class="row-sep" style="top:473px"></span>

  <div class="card" style="left:148px;top:500px;width:632px;height:68px;background:#131515"></div>
  <span class="input" style="left:166px;top:515px;width:597px;height:36px;line-height:34px">Enter E-Mail-Adresse eingeben</span>
  <span class="btn btn-green" style="left:690px;top:523px;width:67px;height:20px;line-height:20px">Hinzufügen</span>
</section>

<section class="screen" style="left:781.1px;top:303.7px;height:621px">
  <header class="topbar">
    <div class="brand"><span class="brand-dot"></span><span class="brand-name">Mailbrook</span></div>
    <p class="greeting">Guten Tag, Lena Hartmann</p>
    <p class="mode">Beobachtungsmodus - Mails werden analysiert aber nicht blockiert</p>
    <span class="chat"><i style="left:5px"></i><i style="left:9px"></i><i style="left:13px"></i></span>
    <svg class="bell" viewBox="0 0 18 18"><path d="M9 2a5 5 0 0 1 5 5v4l2 3H2l2-3V7a5 5 0 0 1 5-5zM7 15a2 2 0 0 0 4 0z" fill="#fff"/></svg>
    <i class="bell-badge">9</i>
    <span class="avatar" role="img" aria-label="Profilfoto des Nutzers"></span>
    <span class="user">Lena Hartmann</span>
    <svg class="caret" viewBox="0 0 8 8"><path d="M1 2.5 4 5.5 7 2.5" stroke="#fff" fill="none"/></svg>
  </header>
  <aside class="sidebar">
    <ul class="nav">
      <li><svg viewBox="0 0 8 8"><path d="M0 0h3v3H0zM5 0h3v3H5zM0 5h3v3H0zM5 5h3v3H5z" fill="currentColor"/></svg>Dashboard</li>
      <li><svg viewBox="0 0 8 8"><path d="M0 1h8M0 4h8M0 7h8" stroke="currentColor"/></svg>Mail-Log</li>
      <li><svg viewBox="0 0 8 8"><path d="M4 .5 7 2v2.5C7 6 5.5 7.2 4 7.6 2.5 7.2 1 6 1 4.5V2z" stroke="currentColor" fill="none"/></svg>Quarantine</li>
      <li><svg viewBox="0 0 8 8"><rect x=".5" y="1.5" width="7" height="5.5" rx="1" stroke="currentColor" fill="none"/></svg>Mailbox Quota</li>
      <li class="active"><svg viewBox="0 0 8 8"><circle cx="4" cy="4" r="3" stroke="currentColor" fill="none"/><circle cx="4" cy="4" r="1" fill="currentColor"/></svg>Settings</li>
      <li><svg viewBox="0 0 8 8"><rect x="1" y="3.5" width="6" height="4" stroke="currentColor" fill="none"/><path d="M2.5 3.5V2a1.5 1.5 0 0 1 3 0v1.5" stroke="currentColor" fill="none"/></svg>Paywall Overlay</li>
      <li><svg viewBox="0 0 8 8"><rect x=".5" y=".5" width="7" height="7" stroke="currentColor" fill="none"/><path d="M3 .5v7" stroke="currentColor"/></svg>Navigation Shell</li>
    </ul>
  </aside>
  <h1 class="page-title">Einstellungen</h1>
  <p class="page-desc" style="width:420px">Verwalten Sie Ihre Kontoeinstellungen und Aufbewahrungsregeln.</p>

  <div class="card" style="left:148px;top:108px;width:632px;height:151px"></div>
  <p class="card-title" style="left:160px;top:120px">Passwort ändern</p>
  <span class="input" style="left:160px;top:151px;width:298px;height:26px;line-height:24px">Aktuelles Passwort</span>
  <span class="input" style="left:469px;top:151px;width:298px;height:26px;line-height:24px">Neues Passwort</span>
  <span class="input" style="left:160px;top:186px;width:298px;height:25px;line-height:23px">Passwort bestätigen</span>
  <span class="btn btn-green" style="left:160px;top:228px;width:90px;height:20px;line-height:20px">Passwort speichern</span>

  <div class="card" style="left:148px;top:272px;width:632px;height:98px"></div>
  <p class="card-title" style="left:160px;top:283px">Aufbewahrungsdauer</p>
  <p style="left:160px;top:315px;font-size:12px;font-weight:300;white-space:nowrap">90 Tage</p>
  <span style="left:219px;top:323px;width:548px;height:2px;background:#2a2e2d"></span>
  <span style="left:219px;top:323px;width:55px;height:2px;background:var(--green)"></span>
  <span style="left:270px;top:319px;width:9px;height:9px;border-radius:50%;background:var(--green-2)"></span>
  <p class="card-text" style="left:160px;top:349px">Legen Sie fest, wie lange zurückgehaltene E-Mails gespeichert werden.</p>

  <div class="card" style="left:148px;top:381px;width:632px;height:58px"></div>
  <p class="card-title" style="left:160px;top:393px">Anonymisierung</p>
  <p class="card-text" style="left:160px;top:419px">Bestimmen Sie, nach wie vielen Tagen Protokolle anonymisiert werden.</p>
  <span class="input" style="left:684px;top:404px;width:83px;height:24px;line-height:22px;color:var(--text);font-size:6px">90<span style="position:absolute;right:8px;top:0">⇕</span></span>

  <div class="card" style="left:148px;top:451px;width:632px;height:142px"></div>
  <p class="card-title" style="left:160px;top:463px">Verhalten bei zu großen E-Mails</p>
  <p class="card-text" style="left:160px;top:489px">Wählen Sie aus, was mit E-Mails passiert, die das Größenlimit überschreiten.</p>
  <div class="opt" style="left:160px">
    <svg viewBox="0 0 11 11"><circle cx="5.5" cy="5.5" r="4.5" stroke="#e0363d" stroke-width="1.2" fill="none"/><path d="M2.3 2.3l6.4 6.4" stroke="#e0363d" stroke-width="1.2"/></svg>
    <span class="opt-radio"></span><span class="opt-title">E-Mail ablehnen</span><span class="opt-desc">E-Mail wird abgelehnt und nicht zugestellt.</span>
  </div>
  <div class="opt" style="left:367px">
    <svg viewBox="0 0 11 11"><circle cx="2.5" cy="8.5" r="1.8" stroke="#e39a1c" fill="none"/><circle cx="2.5" cy="2.5" r="1.8" stroke="#e39a1c" fill="none"/><path d="M4 3.5 10 9M4 7.5 10 2" stroke="#e39a1c"/></svg>
    <span class="opt-radio"></span><span class="opt-title">Zustellen und markieren</span><span class="opt-desc">E-Mail wird zugestellt und als Warnung markiert.</span>
  </div>
  <div class="opt" style="left:573px">
    <svg viewBox="0 0 11 11"><circle cx="5.5" cy="5.5" r="4.5" stroke="#e0363d" stroke-width="1.2" fill="none"/><path d="M2.3 2.3l6.4 6.4" stroke="#e0363d" stroke-width="1.2"/></svg>
    <span class="opt-radio"></span><span class="opt-title">Blockieren</span><span class="opt-desc">E-Mail wird vollständig blockiert.</span>
  </div>
</section>

</body>
</html>
```